YouTube Channel Header Design

YouTube header for company channel. Ridgewell Safety Goods. Looking for technological design for the security industry which includes burglar alarm, fire alarm, cameras, networking and Access Control

```html
<!DOCTYPE html>
<html lang="en">
<head>
<meta charset="utf-8">
<title>Ridgewell Safety Goods – Channel Header Sizes</title>
<link rel="stylesheet" href="https://fonts.googleapis.com/css2?family=Barlow+Semi+Condensed:wght@400;700&family=Oswald:wght@700&display=swap">
<style>
  :root {
    --page-bg: #e4e4e4;
    --label-ink: #4a4548;
    --banner-base: #07060f;
    --banner-red: rgba(226, 18, 58, 0.42);
    --banner-red-soft: rgba(120, 14, 50, 0.25);
    --text-light: #ffffff;
    --accent-yellow: #f2b705;
  }
  * { margin: 0; padding: 0; box-sizing: border-box; }
  html, body {
    width: 1119px;
    height: 1200px;
    overflow: hidden;
    background: var(--page-bg);
  }
  .sheet {
    position: relative;
    width: 1119px;
    height: 1200px;
  }
  .size-label {
    position: absolute;
    left: 0;
    width: 1200px;
    margin-left: -1px;
    text-align: center;
    width: 1119px;
    font-family: "Oswald", "Arial Narrow", sans-serif;
    font-weight: 700;
    font-size: 37px;
    letter-spacing: 5px;
    color: var(--label-ink);
    text-shadow: 0 5px 7px rgba(0, 0, 0, 0.35);
    line-height: 1;
  }
  .size-label--tablet { top: 20px; }
  .size-label--pc { top: 292px; }
  .size-label--tv { top: 571px; }

  .banner {
    position: absolute;
    background: var(--banner-base);
    box-shadow: 0 12px 14px rgba(0, 0, 0, 0.45);
    overflow: hidden;
  }
  .banner--tablet { left: 225px; top: 85px; width: 704px; height: 160px; }
  .banner--pc { left: 91px; top: 348px; width: 972px; height: 161px; }
  .banner--tv { left: 107px; top: 623px; width: 940px; height: 529px; }

  .halftone-field {
    position: absolute;
    inset: 0;
    background:
      repeating-linear-gradient(110deg,
        transparent 0px, transparent 70px,
        var(--banner-red-soft) 90px, var(--banner-red) 125px,
        transparent 150px, transparent 170px),
      var(--banner-base);
    -webkit-mask-image: linear-gradient(to bottom, #000 0%, rgba(0,0,0,0.35) 45%, transparent 90%);
            mask-image: linear-gradient(to bottom, #000 0%, rgba(0,0,0,0.35) 45%, transparent 90%);
  }
  .banner--tablet .halftone-field,
  .banner--pc .halftone-field { opacity: 0.35; }
  .banner--tv .halftone-field {
    -webkit-mask-image: linear-gradient(to bottom, #000 0%, rgba(0,0,0,0.6) 35%, transparent 70%);
            mask-image: linear-gradient(to bottom, #000 0%, rgba(0,0,0,0.6) 35%, transparent 70%);
  }

  .brand-block {
    position: absolute;
    left: 0;
    right: 0;
    text-align: center;
    color: var(--text-light);
    font-family: "Barlow Semi Condensed", "Arial Narrow", sans-serif;
  }
  .banner--tablet .brand-block { top: 37px; padding-left: 12px; }
  .banner--pc .brand-block { top: 37px; padding-left: 12px; }
  .banner--tv .brand-block { top: 230px; padding-left: 42px; }

  .brand-intro {
    font-size: 11.5px;
    font-weight: 400;
    letter-spacing: 2.6px;
    line-height: 14px;
  }
  .brand-name {
    margin-top: 10px;
    font-size: 33px;
    font-weight: 700;
    letter-spacing: 1px;
    line-height: 30px;
    text-transform: uppercase;
  }
  .service-list {
    margin-top: 10px;
    font-size: 11.5px;
    font-weight: 400;
    letter-spacing: 2.2px;
    line-height: 14px;
    white-space: nowrap;
  }
  .service-divider {
    display: inline-block;
    width: 2px;
    height: 10px;
    margin: 0 8px 0 6px;
    background: var(--accent-yellow);
    vertical-align: -1px;
  }
</style>
</head>
<body>
<main class="sheet">

  <h2 class="size-label size-label--tablet">TABLET</h2>
  <section class="banner banner--tablet">
    <div class="halftone-field" role="img" aria-label="Red halftone dot streaks slanting across a dark background"></div>
    <div class="brand-block">
      <p class="brand-intro">THE OFFICIAL CHANNEL OF</p>
      <p class="brand-name">Ridgewell Safety Goods</p>
      <p class="service-list">BURGLAR ALARM<span class="service-divider"></span>FIRE ALARM<span class="service-divider"></span>CAMERAS<span class="service-divider"></span>NETWORKING<span class="service-divider"></span>ACCESS CONTROL</p>
    </div>
  </section>

  <h2 class="size-label size-label--pc">PC</h2>
  <section class="banner banner--pc">
    <div class="halftone-field" role="img" aria-label="Red halftone dot streaks slanting across a dark background"></div>
    <div class="brand-block">
      <p class="brand-intro">THE OFFICIAL CHANNEL OF</p>
      <p class="brand-name">Ridgewell Safety Goods</p>
      <p class="service-list">BURGLAR ALARM<span class="service-divider"></span>FIRE ALARM<span class="service-divider"></span>CAMERAS<span class="service-divider"></span>NETWORKING<span class="service-divider"></span>ACCESS CONTROL</p>
    </div>
  </section>

  <h2 class="size-label size-label--tv">TV</h2>
  <section class="banner banner--tv">
    <div class="halftone-field" role="img" aria-label="Bright red halftone dot streaks slanting down from the top edge over a dark background"></div>
    <div class="brand-block">
      <p class="brand-intro">THE OFFICIAL CHANNEL OF</p>
      <p class="brand-name">Ridgewell Safety Goods</p>
      <p class="service-list">BURGLAR ALARM<span class="service-divider"></span>FIRE ALARM<span class="service-divider"></span>CAMERAS<span class="service-divider"></span>NETWORKING<span class="service-divider"></span>ACCESS CONTROL</p>
    </div>
  </section>

</main>
</body>
</html>
```